Marketing material for IT Company
Brochure/Sales Sheet/Flyer
Brochure will be in two languages, and tri-fold. Would go like this; front (outer) side: first fold: page for information in 2nd languge, second fold: page for information in 2nd language, third fold: cover page in 1st language; back side (inner) side: first fold is for information in 1st language, second fold is for information in 1st language, third fold is cover page for 2nd language.
Information Technology
Brochure view and dimensions are in an uploaded file. Size of flyer equals to size of 1 fold of brochure (i.e one brochure size = 3 flyers size). Size of Sales Sheet is equal to brochure's size. (Sales Sheet won't be folded).
Trifold Brochure view and dimensions
Tulmori logo and Divisions logos (CMYK)
Tulmori logo and Divisions logos (PMS)
Tulmori vertical logo and Divisions vertical logos (CMYK)
Tulmori vertical logo and Divisions vertical logos (PMS)
Tulmori old Brochure (uploaded as an example)
Example of our folder, if it can help
Example of our biz card, if it can help
To help you understand how we see our brochure, one more PIC
Tulmori logo colors information

```html
<!DOCTYPE html>
<html lang="en">
<head>
<meta charset="utf-8">
<title>Tulmori – Rear Cover</title>
<link href="https://fonts.googleapis.com/css2?family=Arimo:wght@400;700&display=swap" rel="stylesheet">
<style>
  :root {
    --page: #f4f5f7;
    --panel-blue: #d8e9f7;
    --panel-edge: #9ec6e6;
    --ink-blue: #1d4f8c;
    --band-blue: #2f86c8;
    --band-deep: #1f6fb0;
    --services-green: #3b9a3f;
    --support-orange: #e58a12;
    --brand-blue: #2a6fb3;
    --card-white: #ffffff;
    --frame-gray: #c9ced6;
    --label-black: #111111;
  }
  * { box-sizing: border-box; margin: 0; padding: 0; }
  html, body { width: 1200px; height: 871px; overflow: hidden; }
  body { background: var(--page); font-family: "Arimo", Arial, sans-serif; position: relative; }

  .inner-spread {
    position: absolute; left: 18px; top: 22px; width: 762px; height: 770px;
    background: var(--panel-blue); border: 2px solid var(--panel-edge); border-radius: 22px;
    overflow: hidden;
  }
  .fold { position: absolute; top: 0; width: 370px; height: 100%; }
  .fold--services { left: 6px; }
  .fold--support { left: 386px; }
  .fold-divider { position: absolute; left: 378px; top: 0; width: 4px; height: 100%; background: #ffffff; opacity: .8; }

  .division-mark {
    position: absolute; left: 24px; top: 22px; width: 320px; height: 108px;
    background: var(--card-white); border-radius: 14px;
    display: flex; align-items: center; justify-content: center; gap: 14px;
  }
  .division-mark .dot { width: 40px; height: 40px; border-radius: 50%; }
  .division-mark .name { font-size: 40px; font-weight: 700; line-height: 1; }
  .division-mark .division { font-size: 18px; font-weight: 700; display: block; margin-top: 4px; }
  .fold--services .dot { background: var(--services-green); }
  .fold--services .name, .fold--services .division { color: var(--services-green); }
  .fold--support .dot { background: var(--support-orange); }
  .fold--support .name, .fold--support .division { color: var(--support-orange); }

  .fold-body {
    position: absolute; left: 26px; top: 148px; width: 320px;
    font-size: 11.6px; line-height: 1.3; color: var(--ink-blue); text-align: justify;
  }

  .mission {
    position: absolute; left: 0; top: 548px; width: 370px; height: 222px;
    background: linear-gradient(180deg, var(--band-blue), var(--band-deep));
    padding: 12px 22px; color: #ffffff;
  }
  .mission h2 { font-size: 16px; font-weight: 700; margin-bottom: 8px; }
  .mission p { font-size: 11.6px; line-height: 1.3; text-align: justify; }

  .cover {
    position: absolute; left: 795px; top: 22px; width: 392px; height: 770px;
    background: var(--card-white); border: 2px solid var(--frame-gray); border-radius: 18px; overflow: hidden;
  }
  .cover-mark {
    position: absolute; left: 28px; top: 28px; display: flex; align-items: center; gap: 16px;
  }
  .cover-mark .dot { width: 62px; height: 62px; border-radius: 50%; background: var(--brand-blue); }
  .cover-mark .name { font-size: 58px; font-weight: 700; color: var(--brand-blue); line-height: 1; }
  .cover-photo { position: absolute; left: 24px; top: 130px; width: 340px; height: 380px; border-radius: 10px; overflow: hidden; }
  .cover-text { position: absolute; left: 26px; top: 530px; width: 336px; color: var(--ink-blue); }
  .cover-text h1 { font-size: 20px; font-weight: 700; line-height: 1.15; }
  .cover-text p { font-size: 13px; line-height: 1.3; text-align: justify; }
  .cover-text p strong { font-size: 20px; }
  .cover-band {
    position: absolute; left: 0; bottom: 0; width: 100%; height: 36px;
    background: linear-gradient(90deg, var(--band-deep), var(--band-blue));
  }

  .sheet-label {
    position: absolute; left: 948px; top: 806px; font-size: 30px; font-weight: 700;
    color: var(--label-black); letter-spacing: .5px;
  }
</style>
</head>
<body>
  <section class="inner-spread">
    <div class="fold fold--services">
      <div class="division-mark">
        <span class="dot"></span>
        <span><span class="name">Tulmori</span><span class="division">services</span></span>
      </div>
      <p class="fold-body">Lorem ipsum dolor sit amet, consectetur adipiscing elit. Suspendisse risus ipsum, placerat porta hendrerit eget, sagittis ut odio. Phasellus malesuada, odio eu euismod sodales, nulla dui viverra mauris, nec luctus mauris risus at purus. Cras tincidunt lorem ac lectus tincidunt vel interdum erat rhoncus. Aliquam at purus a sem vestibulum pulvinar. Pellentesque habitant morbi tristique senectus et netus et malesuada fames ac turpis egestas. Nam eget purus ut ligula ultricies malesuada nec nec arcu. Ut nec urna ac arcu dignissim congue. Morbi sagittis risus sit amet augue placerat vehicula. Vestibulum mauris leo, imperdiet quis tempus in, accumsan non ante. Lorem ipsum dolor sit amet, consectetur adipiscing elit. Suspendisse risus ipsum, placerat porta hendrerit eget, sagittis ut odio. Phasellus malesuada, odio eu euismod sodales, nulla dui viverra mauris, nec luctus mauris risus at purus. Cras tincidunt lorem ac lectus tincidunt vel interdum erat rhoncus. Aliquam at purus a sem vestibulum pulvinar. Pellentesque habitant morbi tristique senectus et netus et malesuada fames ac turpis egestas. Nam eget purus ut ligula ultricies malesuada nec nec arcu. Ut nec urna ac arcu dignissim congue. Morbi sagittis risus sit amet augue placerat vehicula. Vestibulum mauris leo, imperdiet quis tempus in, accumsan non ante.</p>
      <div class="mission">
        <h2>Mission Statement</h2>
        <p>Lorem ipsum dolor sit amet, consectetur adipiscing elit. Suspendisse risus ipsum, placerat porta hendrerit eget, sagittis ut odio. Phasellus malesuada, odio eu euismod sodales, nulla dui viverra mauris, nec luctus mauris risus at purus. Cras tincidunt lorem ac lectus tincidunt vel interdum erat rhoncus. Aliquam at purus a sem vestibulum pulvinar. Pellentesque habitant morbi tristique.</p>
      </div>
    </div>
    <div class="fold-divider"></div>
    <div class="fold fold--support">
      <div class="division-mark">
        <span class="dot"></span>
        <span><span class="name">Tulmori</span><span class="division">support</span></span>
      </div>
      <p class="fold-body">For the brochure we would like the pages to fold outwards periodically (as in uploaded examples). Also we'd like to have it bilingual in both languages. Make sure the languages are implemented so that when viewed from one side and unfolded the information would be in the first language and on the other side in the second, as well as the brochure where you could only read one language when you unfold the outwardly folded brochure. You may use any sample text. For the brochure we would like the pages to fold outwards periodically (as in uploaded examples). Also we'd like to have it bilingual in both languages. Make sure the languages are implemented so that when viewed from one side and unfolded the information would be in the first language and on the other side in the second, as well as the brochure where you could only read one language when you unfold the outwardly folded brochure. You may use any sample text. For the brochure we would like the pages to fold outwards periodically (as in uploaded examples). Also we'd like to have it bilingual in both languages. Make sure the languages are implemented so that when viewed from one side and unfolded the information would be in the first language and on the other side in the second.</p>
      <div class="mission">
        <h2>Mission Statement</h2>
        <p>Brochure will be in two languages, and tri-fold. Would go like this; front (outer) side: first fold: page for information in 2nd language, second fold: page for information in 2nd language, third fold: cover page in 1st language; back (inner) side: first fold is for information in 1st language, second fold is for information in 1st language.</p>
      </div>
    </div>
  </section>

  <section class="cover">
    <div class="cover-mark">
      <span class="dot"></span>
      <span class="name">Tulmori</span>
    </div>
    <svg class="cover-photo" viewBox="0 0 340 380" role="img" aria-label="Photo of a businessman standing on an open laptop with a city skyline against a blue sky">
      <defs>
        <linearGradient id="sky" x1="0" y1="0" x2="0" y2="1">
          <stop offset="0" stop-color="#5fa6dc"/>
          <stop offset=".6" stop-color="#a9d0ee"/>
          <stop offset="1" stop-color="#dfeaf3"/>
        </linearGradient>
      </defs>
      <rect width="340" height="380" fill="url(#sky)"/>
    </svg>
    <div class="cover-text">
      <h1>Lorem ipsum dolor sit</h1>
      <p><strong>amet,</strong> consectetur adipiscing elit. Suspendisse risus ipsum, placerat porta hendrerit eget, sagittis ut odio. Phasellus malesuada, odio eu euismod sodales, nulla dui viverra mauris, nec luctus mauris risus at purus. Cras tincidunt lorem ac lectus tincidunt vel interdum erat rhoncus. Aliquam at purus a sem vestibulum pulvinar. Pellentesque habitant morbi tristique senectus et netus et malesuada fames</p>
    </div>
    <div class="cover-band"></div>
  </section>

  <div class="sheet-label">REAR COVER</div>
</body>
</html>
```